Travelogue book cover

The book is a collection of stories from my travels around the world. These stories run a full range of emotions from unbridled joy, to things that are much funnier today than they were at the time, to moments of sadness while reflecting on places that have been irrevocably changed. This world is an amazing and powerful place, and my stories tell its tale. The overall vibe is to love exploring the world, the thrill of discovery, the comedy of getting outside of your comfort zone, and just generally wanting to convey a sense of wonder and make people feel like they want to get out and explore for themselves.

The audience is in the 30-50 age target, educated, all genders, and either an experienced traveller or wishes they were.

On the style, I am looking for something that stands out when a reader is browsing Brellowmart. Since most book covers are bright, full bleed and busy, I would prefer something that emphasizes white space and simplicity.

```html
<!DOCTYPE html>
<html lang="en">
<head>
<meta charset="utf-8">
<title>My Journey — Book Cover</title>
<link href="https://fonts.googleapis.com/css2?family=Questrial&family=EB+Garamond:wght@400;500&display=swap" rel="stylesheet">
<style>
  :root {
    --canvas: #ffffff;
    --frame: #888888;
    --paper: #ffffff;
    --ink: #111111;
    --olive: #6b6a45;
    --subtitle-ink: #3a2222;
    --ring: #ebebeb;
    --ring-edge: #dcdcdc;
    --placeholder: #b7bfc4;
  }
  * { margin: 0; padding: 0; box-sizing: border-box; }
  html, body { width: 1200px; height: 1200px; overflow: hidden; background: var(--canvas); }
  .canvas { position: relative; width: 1200px; height: 1200px; }
  .artwork { position: absolute; inset: 0; }
  .text { position: absolute; }
  .sans { font-family: "Questrial", "Century Gothic", sans-serif; }
  .serif { font-family: "EB Garamond", Georgia, serif; font-variant: small-caps; }

  .front-author {
    left: 635px; width: 404px; top: 416px; text-align: center;
    font-size: 31px; color: var(--olive); letter-spacing: 0.5px; font-weight: 700;
  }
  .front-title {
    left: 635px; width: 404px; top: 752px; text-align: center;
    font-size: 44px; color: var(--ink); font-weight: 700; letter-spacing: 0.5px;
  }
  .front-subtitle {
    left: 640px; width: 394px; top: 814px; text-align: center;
    font-size: 18px; color: var(--subtitle-ink); letter-spacing: 1.2px; white-space: nowrap;
  }
  .spine-title, .spine-author {
    left: 603px; transform-origin: 0 0; transform: rotate(90deg) translateY(-50%);
    font-size: 29px; font-weight: 700; white-space: nowrap;
  }
  .spine-title { top: 382px; color: var(--ink); }
  .spine-author { top: 678px; color: var(--olive); }
  .back-blurb {
    left: 208px; width: 322px; top: 440px; text-align: center;
    font-size: 14px; line-height: 14.5px; color: var(--ink); letter-spacing: 0.3px;
  }
  .back-blurb .lead { font-size: 16px; }
</style>
</head>
<body>
<div class="canvas">
  <svg class="artwork" width="1200" height="1200" viewBox="0 0 1200 1200">
    <defs>
      <filter id="soft-shadow" x="-20%" y="-50%" width="140%" height="200%">
        <feDropShadow dx="0" dy="2" stdDeviation="2" flood-color="#000" flood-opacity="0.25"/>
      </filter>
    </defs>

    <rect class="frame" x="152" y="299" width="904" height="609" fill="var(--frame)"/>
    <rect class="back-panel" x="168" y="328" width="403" height="551" fill="var(--paper)"/>
    <rect class="spine-panel" x="580" y="328" width="46" height="551" fill="var(--paper)"/>
    <rect class="front-panel" x="635" y="328" width="404" height="551" fill="var(--paper)"/>

    <ellipse class="blurb-ring" cx="368" cy="595" rx="173" ry="180" fill="var(--ring)"
             role="img" aria-label="Faint street map pattern ringing the blurb"/>
    <ellipse class="blurb-disc" cx="368" cy="595" rx="152" ry="157" fill="var(--paper)"/>

    <circle class="globe-ring" cx="832" cy="590" r="116" fill="#f1f1f1" stroke="var(--ring-edge)"
            role="img" aria-label="Street map pattern framing the globe"/>
    <circle class="globe" cx="834" cy="606" r="84" fill="var(--placeholder)"
            role="img" aria-label="Photograph of planet Earth seen from space"/>
    <path class="globe-band" d="M704 598 C745 560 800 578 850 592 C900 606 930 598 961 584 L961 600 C930 616 895 618 848 606 C800 594 750 584 704 612 Z"
          fill="var(--paper)" filter="url(#soft-shadow)"/>

    <path class="title-swoosh" d="M643 817 C720 790 790 792 860 810 C930 828 985 830 1028 790 L1029 816 C990 844 935 846 865 830 C795 814 725 808 643 822 Z"
          fill="var(--paper)" filter="url(#soft-shadow)"/>
  </svg>

  <div class="text sans front-author">RJ Calloway</div>
  <div class="text sans front-title">My Journey</div>
  <div class="text serif front-subtitle">Stories from travels around the world</div>

  <div class="text sans spine-title">My Journey</div>
  <div class="text sans spine-author">RJ Calloway</div>

  <p class="text serif back-blurb"><span class="lead">The</span><br>book is a<br>collection of stories<br>from my travels around the<br>world. <span class="lead">These</span> stories run a full<br>range of emotions from unbridled<br>joy, to things that are much funnier<br>today than they were at the time, to<br>moments of sadness while reflecting on<br>places that have been irrevocably<br>changed. <span class="lead">This</span> world is an amazing and<br>powerful place, and my stories tell its<br>tale. <span class="lead">The</span> overall vibe is to love<br>exploring the world, the thrill of<br>discovery, the comedy of getting<br>outside of your comfort zone, and<br>just generally wanting to convey a<br>sense of wonder and make people<br>feel like they want to get<br>out and explore for<br>themselves.</p>
</div>
</body>
</html>
```